Stonebay Towing Business Card

Towing
Accident towing
Mechanical breakdown
Insurance, salvage and recovery
4wd off road towing
Light & Heavy towing
8347 2516
24 hour business 7 days

Logo can be whole size on front

Industry/Entity Type

Towing/ transport

Contact Information for Business Card

The above

```html
<!DOCTYPE html>
<html lang="en">
<head>
<meta charset="utf-8">
<title>Stonebay Towing Business Card</title>
<link rel="stylesheet" href="https://fonts.googleapis.com/css2?family=Bebas+Neue&family=Poppins:wght@400;700&display=swap">
<style>
  :root {
    --backdrop: #c3c3c3;
    --card: #ffffff;
    --brand-red: #d31f27;
    --ink: #111111;
    --ghost: rgba(211, 31, 39, 0.07);
  }
  * { margin: 0; padding: 0; box-sizing: border-box; }
  html, body {
    width: 1093px;
    height: 1200px;
    overflow: hidden;
    background: var(--backdrop);
  }
  .canvas {
    position: relative;
    width: 1093px;
    height: 1200px;
  }
  .card {
    position: absolute;
    left: 264px;
    width: 580px;
    height: 357px;
    background: var(--card);
    overflow: hidden;
  }
  .card--front { top: 226px; }
  .card--back { top: 620px; }

  .front-wave {
    position: absolute;
    inset: 0;
    width: 100%;
    height: 100%;
  }
  .ghost-name {
    position: absolute;
    left: 180px;
    top: 120px;
    width: 380px;
    text-align: center;
    font-family: "Bebas Neue", sans-serif;
    font-size: 86px;
    line-height: 1;
    color: var(--ghost);
  }
  .services {
    position: absolute;
    left: 162px;
    top: 34px;
    list-style: none;
  }
  .services__item {
    display: flex;
    align-items: center;
    height: 41.2px;
    font-family: "Bebas Neue", sans-serif;
    font-size: 27px;
    color: var(--ink);
    letter-spacing: 0.2px;
  }
  .services__icon {
    width: 24px;
    height: 24px;
    margin-right: 14px;
    flex: none;
  }
  .contact {
    position: absolute;
    left: 163px;
    top: 297px;
    display: flex;
    align-items: center;
  }
  .contact__icon { width: 29px; height: 29px; margin-right: 4px; }
  .contact__phone {
    font-family: "Poppins", sans-serif;
    font-weight: 700;
    font-size: 27px;
    letter-spacing: 3px;
    color: var(--brand-red);
    line-height: 1;
  }
  .hours {
    position: absolute;
    left: 380px;
    top: 294px;
    width: 200px;
    height: 37px;
    background: var(--brand-red);
    border-radius: 19px 0 0 19px;
    display: flex;
    align-items: center;
    padding-left: 25px;
    font-family: "Poppins", sans-serif;
    font-size: 13px;
    color: #ffffff;
  }
  .brand-name {
    position: absolute;
    inset: 0;
    display: flex;
    align-items: center;
    justify-content: center;
    font-family: "Bebas Neue", sans-serif;
    font-size: 78px;
    color: var(--brand-red);
    letter-spacing: 1px;
  }
</style>
</head>
<body>
<main class="canvas">
  <section class="card card--front">
    <svg class="front-wave" viewBox="0 0 580 357" preserveAspectRatio="none" aria-hidden="true">
      <path d="M0 0 H115 C130 40 140 80 128 130 C115 190 92 230 92 275 C92 315 104 340 120 357 H0 Z" fill="var(--ink)"/>
      <path d="M0 0 H107 C121 40 131 80 119 130 C106 190 83 230 83 275 C83 315 95 340 109 357 H0 Z" fill="var(--brand-red)"/>
      <path d="M72 0 C84 50 88 100 76 150 C64 200 50 240 52 285 C54 320 62 340 72 357" fill="none" stroke="#b51a21" stroke-width="1"/>
    </svg>

    <div class="ghost-name" aria-hidden="true">Stonebay Towing</div>

    <ul class="services">
      <li class="services__item"><svg class="services__icon" viewBox="0 0 24 24"><circle cx="11" cy="12" r="9" fill="none" stroke="var(--brand-red)" stroke-width="1.2"/><path d="M17 4 L23 12 L17 20" fill="none" stroke="var(--brand-red)" stroke-width="1.2"/><circle cx="11" cy="12" r="6" fill="none" stroke="var(--brand-red)" stroke-width="1.2"/><path d="M11 8.5 L14.5 12 L11 15.5 L7.5 12 Z" fill="var(--brand-red)"/></svg>Towing</li>
      <li class="services__item"><svg class="services__icon" viewBox="0 0 24 24"><circle cx="11" cy="12" r="9" fill="none" stroke="var(--brand-red)" stroke-width="1.2"/><path d="M17 4 L23 12 L17 20" fill="none" stroke="var(--brand-red)" stroke-width="1.2"/><circle cx="11" cy="12" r="6" fill="none" stroke="var(--brand-red)" stroke-width="1.2"/><path d="M11 8.5 L14.5 12 L11 15.5 L7.5 12 Z" fill="var(--brand-red)"/></svg>Accident Towing</li>
      <li class="services__item"><svg class="services__icon" viewBox="0 0 24 24"><circle cx="11" cy="12" r="9" fill="none" stroke="var(--brand-red)" stroke-width="1.2"/><path d="M17 4 L23 12 L17 20" fill="none" stroke="var(--brand-red)" stroke-width="1.2"/><circle cx="11" cy="12" r="6" fill="none" stroke="var(--brand-red)" stroke-width="1.2"/><path d="M11 8.5 L14.5 12 L11 15.5 L7.5 12 Z" fill="var(--brand-red)"/></svg>Mechanical Breakdown</li>
      <li class="services__item"><svg class="services__icon" viewBox="0 0 24 24"><circle cx="11" cy="12" r="9" fill="none" stroke="var(--brand-red)" stroke-width="1.2"/><path d="M17 4 L23 12 L17 20" fill="none" stroke="var(--brand-red)" stroke-width="1.2"/><circle cx="11" cy="12" r="6" fill="none" stroke="var(--brand-red)" stroke-width="1.2"/><path d="M11 8.5 L14.5 12 L11 15.5 L7.5 12 Z" fill="var(--brand-red)"/></svg>Insurance, Salvage and Recovery</li>
      <li class="services__item"><svg class="services__icon" viewBox="0 0 24 24"><circle cx="11" cy="12" r="9" fill="none" stroke="var(--brand-red)" stroke-width="1.2"/><path d="M17 4 L23 12 L17 20" fill="none" stroke="var(--brand-red)" stroke-width="1.2"/><circle cx="11" cy="12" r="6" fill="none" stroke="var(--brand-red)" stroke-width="1.2"/><path d="M11 8.5 L14.5 12 L11 15.5 L7.5 12 Z" fill="var(--brand-red)"/></svg>4WD Off Road Towing</li>
      <li class="services__item"><svg class="services__icon" viewBox="0 0 24 24"><circle cx="11" cy="12" r="9" fill="none" stroke="var(--brand-red)" stroke-width="1.2"/><path d="M17 4 L23 12 L17 20" fill="none" stroke="var(--brand-red)" stroke-width="1.2"/><circle cx="11" cy="12" r="6" fill="none" stroke="var(--brand-red)" stroke-width="1.2"/><path d="M11 8.5 L14.5 12 L11 15.5 L7.5 12 Z" fill="var(--brand-red)"/></svg>Light &amp; Heavy Towing</li>
    </ul>

    <div class="contact">
      <svg class="contact__icon" viewBox="0 0 30 30" aria-hidden="true">
        <circle cx="15" cy="15" r="14.5" fill="var(--ink)"/>
        <path d="M11.5 9.5 L13.5 9 L14.5 12 L13 13 C13.6 14.6 15 16 16.6 16.6 L17.6 15.2 L20.5 16.3 L20 18.4 C15 19.5 10.2 14.6 11.5 9.5 Z" fill="#ffffff"/>
      </svg>
      <span class="contact__phone">8347 2516</span>
    </div>

    <div class="hours">24 hour business 7 days</div>
  </section>

  <section class="card card--back">
    <h1 class="brand-name">Stonebay Towing</h1>
  </section>
</main>
</body>
</html>
```